Dr Tasneer's Letterhead

I need a professional neat letterhead incorporating my professional information, university titles and qualifications. I have attached my 3 recent ones which contain all the necessary information that needs to be included. I am happy for the information to be a side bar left or right, or as a header/footer combination.

Hello all

I have now made a 2nd and 3rd prize so please submit

Reason: Now there is a 2nd and 3rd place so I can take 3 designs

Industry/Entity Type

University

```html
<!DOCTYPE html>
<html lang="en">
<head>
<meta charset="utf-8">
<title>Dr. Kamran Tasneer – Letterhead</title>
<link rel="stylesheet" href="https://fonts.googleapis.com/css2?family=Libre+Franklin:ital,wght@0,400;1,300&family=Arimo:ital,wght@1,700&display=swap">
<style>
  :root {
    --paper: #ffffff;
    --ink-dark: #333333;
    --ink-mid: #5a5a5a;
    --ink-light: #8a8a8a;
    --rule: #7a7a7a;
  }
  html, body {
    margin: 0;
    padding: 0;
    overflow: hidden;
    background: var(--paper);
  }
  .letterhead {
    position: relative;
    width: 928px;
    height: 1200px;
    background: var(--paper);
    overflow: hidden;
  }
  .doctor-name {
    position: absolute;
    top: 168px;
    left: 0;
    width: 874px;
    margin: 0;
    text-align: center;
    font-family: "Libre Franklin", sans-serif;
    font-weight: 400;
    font-size: 34px;
    line-height: 40px;
    color: var(--ink-dark);
  }
  .rule {
    position: absolute;
    height: 2px;
    background: var(--rule);
  }
  .rule--header { top: 219px; left: 103px; width: 685px; }
  .rule--contact { top: 456px; left: 177px; width: 537px; }
  .credentials {
    position: absolute;
    top: 242px;
    left: 0;
    width: 874px;
    margin: 0;
    text-align: center;
    font-family: "Arimo", sans-serif;
    font-style: italic;
    font-weight: 700;
    font-size: 14.5px;
    line-height: 18.3px;
    color: var(--ink-mid);
  }
  .credentials p { margin: 0; }
  .contact {
    position: absolute;
    top: 495px;
    left: 0;
    width: 884px;
    text-align: center;
    font-family: "Libre Franklin", sans-serif;
    font-style: italic;
    font-weight: 300;
    font-size: 14.5px;
    line-height: 18px;
    color: var(--ink-light);
  }
  .contact p { margin: 0; }
  .phones {
    position: absolute;
    top: 567px;
    left: 0;
    width: 928px;
    font-family: "Libre Franklin", sans-serif;
    font-style: italic;
    font-weight: 300;
    font-size: 14.5px;
    line-height: 18px;
    color: var(--ink-light);
  }
  .phones span { position: absolute; white-space: nowrap; }
  .phone-main { left: 269px; top: 0; }
  .phone-alt { left: 316px; top: 18px; }
  .fax { left: 506px; top: 0; }
</style>
</head>
<body>
  <main class="letterhead">
    <h1 class="doctor-name">Dr. Kamran Tasneer</h1>
    <div class="rule rule--header"></div>

    <section class="credentials">
      <p>BSc Med, MBBS(Hons 1) NSU, MSc, FRACS (Oto-HNS)</p>
      <p>Consultant ENT/Head and Neck Surgeon</p>
      <p>Harbourview Cancer Centre</p>
      <p>Eastbrook Hospital and Eastbrook Local Health District (ELHD)</p>
      <p>Senior Lecturer, Coastal University (CU) &amp; Inland Ridge (UIR)</p>
    </section>

    <div class="rule rule--contact"></div>

    <address class="contact">
      <p>Suite 210/48 Marlow Road, Eastbrook 2150</p>
      <p>7 Kestrel Highway, Ashgrove 2162</p>
      <p>19 Pemberton Street, Riverton 2759</p>
    </address>

    <div class="phones">
      <span class="phone-main">Phone: 95510482</span>
      <span class="phone-alt">95287361</span>
      <span class="fax">Fax: 95443019</span>
    </div>
  </main>
</body>
</html>
```